New webpage design for development bureau

We are a development bureau in Denmark, and need a design for our webpage. We are called Harbor Development (Part of Harbor Fjeld Skolium Group), and are going to aim for multiple markets: Web, Apps, Desktop applications, ect.

We already have a logo, see the uploaded file. We do not have any special demands, other than in have to be simple. A portfolio view should also be available, for future customers.

```html
<!DOCTYPE html>
<html lang="en">
<head>
<meta charset="utf-8">
<title>Harbor Development</title>
<link rel="stylesheet" href="https://fonts.googleapis.com/css2?family=Open+Sans:wght@400;600;700&family=Source+Sans+3:wght@400;600&display=swap">
<style>
:root{
  --blue:#2f7cc0;
  --blue-dark:#1f5f99;
  --ink:#555;
  --ink-soft:#777;
  --ink-light:#999;
  --rule:#e3e3e3;
  --hero:#e4e4e4;
  --footer:#4a4d50;
  --footer-base:#3a3c3e;
  --footer-text:#a9acae;
  --white:#fff;
  --dark-icon:#3b3b3b;
}
*{box-sizing:border-box;margin:0;padding:0}
html,body{width:1085px;height:1200px;overflow:hidden;background:var(--white)}
body{position:relative;font-family:"Open Sans",Arial,sans-serif;color:var(--ink)}
.abs{position:absolute}
ul{list-style:none}

/* header */
.site-header{position:absolute;left:0;top:0;width:1085px;height:55px;background:var(--white);border-top:3px solid #eee;box-shadow:0 1px 2px rgba(0,0,0,.08)}
.brand{position:absolute;left:266px;top:14px;font-size:26px;font-weight:400;letter-spacing:2px;color:#333}
.main-nav{position:absolute;left:557px;top:0;height:55px;display:flex}
.main-nav a{display:block;height:52px;line-height:58px;padding:0 13px;font-size:9px;font-weight:700;color:#333;text-decoration:none;letter-spacing:.3px}
.main-nav a.is-current{background:#f1f1f1;color:var(--blue);border-top:3px solid var(--blue);line-height:52px;padding:0 17px}

/* hero */
.hero{position:absolute;left:0;top:55px;width:1085px;height:231px;background:radial-gradient(ellipse at 45% 60%,#efefef 0%,var(--hero) 60%,#d9d9d9 100%)}
.hero-title{position:absolute;left:266px;top:78px;font-size:16px;line-height:20px;color:#555;letter-spacing:1.5px;white-space:nowrap}
.hero-title b{font-weight:700}
.hero-sub{position:absolute;left:267px;top:101px;font-family:"Source Sans 3",sans-serif;font-size:13.5px;line-height:17px;color:var(--blue);white-space:nowrap}
.hero-rule{position:absolute;left:267px;top:124px;width:208px;height:1px;background:#c8c8c8}
.hero-arrow{position:absolute;top:170px;width:16px;height:16px;border-radius:50%}
.hero-devices{position:absolute;left:600px;top:47px;width:259px;height:142px;border-radius:4px;background:linear-gradient(180deg,#3c3c3c 0%,#d9dde2 45%,#bfc4c9 100%)}

/* intro */
.intro-title{position:absolute;left:0;width:1085px;top:306px;text-align:center;font-size:14px;line-height:18px;font-weight:400;color:#555}
.intro-text{position:absolute;left:0;width:1085px;top:326px;text-align:center;font-size:8.5px;line-height:12px;color:var(--ink-light)}
.rule{position:absolute;left:266px;width:593px;height:1px;background:var(--rule)}

/* features */
.feature-icon{position:absolute;top:385px;width:42px;height:42px;border-radius:50%}
.feature-title{position:absolute;top:381px;font-size:8.5px;font-weight:700;color:#444}
.feature-title.is-active{color:var(--blue)}
.feature-list{position:absolute;top:405px;font-size:7.5px;color:#666}
.feature-list li{height:16px;padding-left:14px;position:relative}
.feature-list li::before{content:"»";position:absolute;left:0;top:-1px;color:#aaa}

/* section heads */
.section-head{position:absolute;font-size:10px;font-weight:700;color:#555}
.pager{position:absolute;font-size:10px;color:#aaa;letter-spacing:3px}
.pager.blue{color:var(--blue)}

/* works */
.work{position:absolute;top:530px;width:136px}
.work-thumb{width:136px;height:96px;border:1px solid #ddd;padding:3px;background:var(--white)}
.work-thumb div{width:100%;height:100%}
.work-title{text-align:center;margin-top:8px;font-size:9.5px;color:#666}
.work-title.is-hover{color:var(--blue);text-decoration:underline}
.work-desc{text-align:center;margin-top:5px;font-size:7.5px;color:#666;padding-bottom:6px;border-bottom:1px solid var(--rule)}

/* cta */
.cta{position:absolute;left:266px;top:692px;width:593px;height:44px;border:1px solid #ddd}
.cta-lead{position:absolute;left:21px;top:11px;font-size:7.5px;font-weight:700;color:#444}
.cta-note{position:absolute;left:21px;top:23px;font-size:6px;color:#aaa}
.cta-button{position:absolute;left:448px;top:9px;width:98px;height:21px;border-radius:2px;background:var(--blue);color:var(--white);font-size:7.5px;font-weight:700;text-align:center;line-height:21px}

/* blog */
.post{position:absolute;top:786px;width:135px}
.post-thumb{width:135px;height:96px;border:1px solid #ddd;padding:3px;position:relative}
.post-thumb .photo{width:100%;height:100%;background:radial-gradient(circle at 60% 55%,#3a6fb3 0%,#1c2740 45%,#0c0f17 100%)}
.post-meta{margin-top:8px;font-size:6.5px;color:#888;font-style:italic}
.post-meta a{color:var(--blue);text-decoration:none}
.post-text{margin-top:8px;font-size:6.8px;line-height:10px;color:#666;padding-bottom:8px;border-bottom:1px solid var(--rule)}
.post-badge{position:absolute;left:3px;right:3px;bottom:3px;height:18px;background:rgba(0,0,0,.55);color:var(--white);font-size:6.5px;display:flex;justify-content:space-between;align-items:center;padding:0 6px}

/* testimonial */
.quote{position:absolute;left:704px;top:786px;width:155px;height:64px;border:1px solid #ddd;padding:9px 12px;font-size:7px;line-height:9.5px;color:#888}
.quote-author{position:absolute;left:768px;top:864px;font-size:7px;color:#888;line-height:10px}
.quote-author strong{color:var(--blue);font-size:8px;display:block}

/* footer */
.site-footer{position:absolute;left:0;top:962px;width:1085px;height:204px;background:var(--footer);color:var(--footer-text)}
.footer-base{position:absolute;left:0;top:1166px;width:1085px;height:34px;background:var(--footer-base);color:#888;font-size:6.5px;padding:12px 0 0 266px}
.footer-brand{position:absolute;left:266px;top:36px;font-size:19px;letter-spacing:2px;color:var(--white)}
.footer-head{position:absolute;top:38px;font-size:8px;font-weight:700;color:#ddd}
.footer-post{position:absolute;left:412px;width:135px;font-size:6.5px;line-height:9px}
.footer-post .date{font-size:6px;color:#bbb}
.footer-post .title{color:#8fc3ef;font-size:7.5px;margin:4px 0 4px}
.contact-row{position:absolute;left:576px;font-size:7.5px;line-height:10px}
.contact-row strong{color:#ddd}
.contact-icon{position:absolute;left:-19px;top:1px}
.newsletter-input{position:absolute;left:734px;top:88px;width:86px;height:25px;background:#3b3d40;border:1px solid #5a5d60}
.newsletter-button{position:absolute;left:820px;top:88px;width:39px;height:25px;background:#5a5d60;color:#ccc;font-size:6.5px;text-align:center;line-height:25px}
.social{position:absolute;top:152px;width:15px;height:15px;border-radius:50%;background:#8c8f92}
</style>
</head>
<body>

<header class="site-header">
  <div class="brand">HARBOR</div>
  <nav class="main-nav">
    <a class="is-current">HOME</a>
    <a>ABOUT US</a>
    <a>SERVICES</a>
    <a>BLOGS</a>
    <a>CONTACT US</a>
  </nav>
</header>

<section class="hero">
  <div class="hero-title"><b>COMPREHENSIVE</b> TECHNOLOGY</div>
  <div class="hero-sub">Powering the next generation of events</div>
  <div class="hero-rule"></div>
  <svg class="hero-arrow" style="left:269px" viewBox="0 0 16 16"><circle cx="8" cy="8" r="8" fill="#3a86c8"/><path d="M9.5 5 6.5 8l3 3" stroke="#fff" stroke-width="1.4" fill="none"/></svg>
  <svg class="hero-arrow" style="left:287px" viewBox="0 0 16 16"><circle cx="8" cy="8" r="8" fill="#444"/><path d="M6.5 5l3 3-3 3" stroke="#fff" stroke-width="1.4" fill="none"/></svg>
  <div class="hero-devices" role="img" aria-label="Website shown on desktop, tablet and phone screens"></div>
</section>

<h1 class="intro-title">Delivering EXCELLENCE, Righteously</h1>
<p class="intro-text">We are committed to excellence through the systematic and disciplined process. We commit to quality outcomes.</p>
<div class="rule" style="top:352px"></div>

<section class="features">
  <svg class="feature-icon" style="left:267px" viewBox="0 0 42 42"><circle cx="21" cy="21" r="20" fill="#3a86c8" stroke="#cfd9e3" stroke-width="2"/><circle cx="24" cy="18" r="5" fill="none" stroke="#fff" stroke-width="2"/><circle cx="16" cy="26" r="3" fill="none" stroke="#fff" stroke-width="2"/></svg>
  <div class="feature-title is-active" style="left:328px">LOREM IPSUM IS SIMPLY</div>
  <ul class="feature-list" style="left:326px"><li>Lorem Ipsum is dumy text</li><li>Virtual Shops &amp; ecommerce</li><li>Content Management System</li><li>Web Design &amp; Development</li></ul>

  <svg class="feature-icon" style="left:484px" viewBox="0 0 42 42"><circle cx="21" cy="21" r="20" fill="var(--dark-icon)" stroke="#ccc" stroke-width="2"/><rect x="15" y="20" width="12" height="9" rx="1" fill="#fff"/><path d="M17 20v-3a4 4 0 0 1 8 0v3" stroke="#fff" stroke-width="2" fill="none"/></svg>
  <div class="feature-title" style="left:545px">LOREM IPSUM IS SIMPLY</div>
  <ul class="feature-list" style="left:543px"><li>Lorem Ipsum is dumy text</li><li>Virtual Shops &amp; ecommerce</li><li>Content Management System</li><li>Web Design &amp; Development</li></ul>

  <svg class="feature-icon" style="left:701px" viewBox="0 0 42 42"><circle cx="21" cy="21" r="20" fill="var(--dark-icon)" stroke="#ccc" stroke-width="2"/><circle cx="21" cy="21" r="8" fill="none" stroke="#fff" stroke-width="3"/><circle cx="21" cy="21" r="3.5" fill="var(--dark-icon)"/></svg>
  <div class="feature-title" style="left:761px">LOREM IPSUM IS SIMPLY</div>
  <ul class="feature-list" style="left:759px"><li>Lorem Ipsum is dumy text</li><li>Virtual Shops &amp; ecommerce</li><li>Content Management System</li><li>Web Design &amp; Development</li></ul>
</section>

<div class="rule" style="top:492px"></div>
<div class="pager" style="left:846px;top:494px">« »</div>

<h2 class="section-head" style="left:266px;top:505px">RECENT WORKS</h2>
<section class="works">
  <article class="work" style="left:266px"><div class="work-thumb"><div role="img" aria-label="Close-up of a payment card chip" style="background:linear-gradient(135deg,#c9a24a 0%,#6b6e74 40%,#3c3f45 100%)"></div></div><div class="work-title">Project Title</div><div class="work-desc">Lorem Ipsum is simply dummy</div></article>
  <article class="work" style="left:420px"><div class="work-thumb"><div role="img" aria-label="Project preview with zoom and link overlay" style="background:linear-gradient(135deg,#5d9bd3 0%,#3a7ec0 60%,#2e6aa8 100%)"></div></div><div class="work-title is-hover">Project Title</div><div class="work-desc">Lorem Ipsum is simply dummy</div></article>
  <article class="work" style="left:573px"><div class="work-thumb"><div role="img" aria-label="Keyboard keys lit in blue" style="background:radial-gradient(circle at 60% 55%,#3a6fb3 0%,#1c2740 45%,#0c0f17 100%)"></div></div><div class="work-title">Project Title</div><div class="work-desc">Lorem Ipsum is simply dummy</div></article>
  <article class="work" style="left:723px"><div class="work-thumb"><div role="img" aria-label="Close-up of a payment card chip" style="background:linear-gradient(135deg,#c9a24a 0%,#6b6e74 40%,#3c3f45 100%)"></div></div><div class="work-title">Project Title</div><div class="work-desc">Lorem Ipsum is simply dummy</div></article>
</section>

<section class="cta">
  <div class="cta-lead">Lorem Ipsum is simply dummy text of the printing and typesetting industry.</div>
  <div class="cta-note">Text of the printing and typesetting industry. Lorem Ipsum has been the industry's standard dummy text ever since the 1500s</div>
  <div class="cta-button">Call to Action Button</div>
</section>

<h2 class="section-head" style="left:266px;top:759px">LATEST FROM THE BLOG</h2>
<div class="pager blue" style="left:669px;top:759px">‹ ›</div>
<section class="blog">
  <article class="post" style="left:266px"><div class="post-thumb"><div class="photo" role="img" aria-label="Keyboard keys lit in blue"></div><div class="post-badge"><span>25 June, 2014</span><span>Website, News</span></div></div><div class="post-meta">By <a>Velmora Technology</a> | 4 Comments</div><div class="post-text">Survived not only five centuries, but also the leap into electronic typesetting</div></article>
  <article class="post" style="left:412px"><div class="post-thumb"><div class="photo" role="img" aria-label="Keyboard keys lit in blue"></div></div><div class="post-meta">By <a>Velmora Technology</a> | 4 Comments</div><div class="post-text">Survived not only five centuries, but also the leap into electronic typesetting</div></article>
  <article class="post" style="left:557px"><div class="post-thumb"><div class="photo" role="img" aria-label="Keyboard keys lit in blue"></div></div><div class="post-meta">By <a>Velmora Technology</a> | 4 Comments</div><div class="post-text">Survived not only five centuries, but also the leap into electronic typesetting</div></article>
</section>

<h2 class="section-head" style="left:704px;top:759px">TESTIMONIAL</h2>
<div class="pager blue" style="left:843px;top:759px">‹ ›</div>
<blockquote class="quote">Lorem Ipsum is simply dummy text of the printing and typesetting industry. Lorem Ipsum has been the industry's standard dummy text ever since</blockquote>
<svg class="abs" style="left:751px;top:842px" width="20" height="18" viewBox="0 0 20 18"><path d="M1 1h13v9H7l-4 3v-3H1z" fill="#333"/><path d="M16 5h3v9h-2v3l-4-3H8v-2" fill="#333"/></svg>
<div class="abs" role="img" aria-label="Client portrait" style="left:711px;top:858px;width:44px;height:44px;border-radius:50%;border:2px solid #ddd;background:#bdbdbd"></div>
<div class="quote-author"><strong>MERILA</strong>Business Development<br>Velmora Technology</div>

<footer class="site-footer">
  <div class="footer-brand">HARBOR</div>

  <div class="footer-head" style="left:412px">RECENT POST</div>
  <div class="footer-post" style="top:58px"><div class="date">JUNE 21, 2014 &nbsp;|&nbsp; BY ADMIN</div><div class="title">Lorem Ipsum is simply dummy text</div>Lorem Ipsum is simply dummy text of the printing and typesetting industryprinting</div>
  <div class="footer-post" style="top:122px"><div class="date">JUNE 21, 2014 &nbsp;|&nbsp; BY ADMIN</div><div class="title">Lorem Ipsum is simply dummy text</div>Lorem Ipsum is simply dummy text of the printing and typesetting industryprinting and typesetting industry</div>

  <div class="footer-head" style="left:576px">CONTACTS</div>
  <div class="contact-row" style="top:59px"><svg class="contact-icon" width="12" height="11" viewBox="0 0 12 11"><path d="M6 0 0 5h2v6h3V7h2v4h3V5h2z" fill="#aaa"/></svg><strong>Harbor INC</strong><br>PO Box 4410<br>Kajgade 12, Aarhus<br>Midtjylland 8000, Denmark</div>
  <div class="contact-row" style="top:113px"><svg class="contact-icon" width="11" height="12" viewBox="0 0 11 12"><path d="M2 0h2l1 3-1.5 1.2a7 7 0 0 0 3.3 3.3L8 6l3 1v2l-1.5 2C5 11 0 6 0 1.5z" fill="#aaa"/></svg>Phone: (555) 014 220 3391<br><span style="line-height:16px">Fax: (555) 014 22034 00</span></div>
  <div class="contact-row" style="top:150px"><svg class="contact-icon" width="12" height="9" viewBox="0 0 12 9"><rect width="12" height="9" fill="#aaa"/><path d="M0 0l6 5 6-5" stroke="#4a4d50" fill="none"/></svg>info@harbor-dev.example</div>

  <div class="footer-head" style="left:734px">NEWSLETTER SIGNUP</div>
  <div class="abs" style="left:734px;top:61px;width:125px;font-size:6.5px;line-height:9px">By subscribing to our mailing list you will get the latest news from us.</div>
  <div class="newsletter-input"></div>
  <div class="newsletter-button">JOIN US</div>

  <div class="footer-head" style="left:734px;top:131px">SOCIAL LINKS</div>
  <div class="social" style="left:735px;background:#3a86c8"></div>
  <div class="social" style="left:753px"></div>
  <div class="social" style="left:772px"></div>
  <div class="social" style="left:791px"></div>
</footer>
<div class="footer-base">Copyright © 2014 Harbor Inc. Design By Velmora</div>

</body>
</html>
```